The Marlow Method Diet Business Card

The Marlow Method is a revolutionary new diet approach. We need a fresh, different business card design for The Marlow Method. We would like the cards lettering and designed match with the color scheme of the logo(Orange,black,grey) and the website. We would like the front of the business card to be the pic of a scale(that people weigh themselves on).We have attached a pic we would like that kind of old school number scale. With the the words "want to lose weight?Eat what you crave! Change how it's made! Get moving! No gym required. Similar to our shirt design. At the Back of the card we would like our logo. My name Dwight Pemberly Jr. My telephone number 504-617-2254 my email dpemberlyjr@marlowmethod.example

Target Market(s)

Everyone who's looking to get into shape

Industry/Entity Type

Health And Wellness

Contact Information for Business Card

Name , company logo, weight scale. Want to have something people talk about that looks so refreshing

Colors
faa54b
f68d4d
000000
b2b2b2

Requirements
Must have
• Weight scale, logo and futuristic look. Nothing plain get creative baby!
Nice to have
• Something that would stand out in a crowd
Should not have
• Be boring or look like any other card or be anything like Brennick diet cards

```html
<!DOCTYPE html>
<html lang="en">
<head>
<meta charset="utf-8">
<title>The Marlow Method – Business Card</title>
<link rel="stylesheet" href="https://fonts.googleapis.com/css2?family=Exo+2:wght@600&family=Jura:wght@400&family=Mulish:wght@700&family=Questrial&display=swap">
<style>
  :root {
    --orange: #faa54b;
    --orange-deep: #f68d4d;
    --black: #231f20;
    --ink: #000000;
    --grey: #b2b2b2;
    --text-grey: #555555;
    --white: #ffffff;
    --stage: #4a4a4a;
  }
  * { margin: 0; padding: 0; box-sizing: border-box; }
  html, body { width: 1105px; height: 1200px; overflow: hidden; }
  body { background: var(--stage); position: relative; font-family: "Questrial", sans-serif; }

  .card {
    position: absolute;
    left: 196px;
    width: 720px;
    height: 412px;
    border-radius: 24px;
    overflow: hidden;
  }
  .card--front { top: 146px; background: var(--white); }
  .card--back { top: 602px; background: var(--black); }

  /* front */
  .front__band {
    position: absolute; left: 0; top: 0; width: 100%; height: 112px;
    background: var(--black);
  }
  .front__name {
    position: absolute; right: 36px; top: 30px;
    font-family: "Exo 2", sans-serif; font-weight: 600; font-size: 27px;
    color: var(--orange);
  }
  .brand {
    position: absolute; left: 34px; top: 178px;
    display: flex; align-items: center; gap: 14px;
  }
  .brand__dot {
    width: 44px; height: 44px; border-radius: 50%; background: var(--orange);
  }
  .brand__name {
    font-family: "Jura", sans-serif; font-weight: 400; font-size: 34px;
    color: var(--text-grey); line-height: 1;
  }
  .contact {
    position: absolute; font-size: 19px; color: var(--text-grey);
  }
  .contact--phone { left: 34px; top: 327px; }
  .contact--phone .label { color: var(--orange-deep); }
  .contact--email { left: 34px; top: 357px; }
  .contact--web { right: 36px; top: 357px; }

  /* back */
  .back__title {
    position: absolute; left: 36px; top: 44px;
    font-family: "Jura", sans-serif; font-weight: 400; color: var(--white);
    line-height: 1;
  }
  .back__title .small { display: block; font-size: 27px; }
  .back__title .large { display: block; font-size: 52px; margin-top: 2px; }
  .back__title .medium { display: block; font-size: 36px; margin-top: 2px; }

  .pitch { position: absolute; left: 40px; top: 206px; color: var(--white); }
  .pitch__heading {
    font-family: "Mulish", sans-serif; font-weight: 700; font-size: 23px;
    letter-spacing: 0.3px; margin-bottom: 12px;
  }
  .pitch__list { list-style: none; font-size: 21px; line-height: 33px; }

  .back__mark-area {
    position: absolute; right: 0; top: 0; width: 380px; height: 412px;
  }
</style>
</head>
<body>

  <section class="card card--front">
    <div class="front__band"></div>
    <div class="front__name">Dwight Pemberly Jr.</div>

    <div class="brand">
      <span class="brand__dot"></span>
      <span class="brand__name">The Marlow Method</span>
    </div>

    <div class="contact contact--phone"><span class="label">P:</span> 504-617-2254</div>
    <div class="contact contact--email">dpemberlyjr@marlowmethod.example</div>
    <div class="contact contact--web">www.marlowmethod.example</div>
  </section>

  <section class="card card--back">
    <div class="back__title">
      <span class="small">The</span>
      <span class="large">Marlow</span>
      <span class="medium">Method</span>
    </div>

    <div class="pitch">
      <p class="pitch__heading">WANT TO LOSE WEIGHT?</p>
      <ul class="pitch__list">
        <li>Eat what you crave!</li>
        <li>Change how it's made!</li>
        <li>Get moving!</li>
        <li>No gym required.</li>
      </ul>
    </div>

    <svg class="back__mark-area" viewBox="0 0 380 412" role="img" aria-label="Large white brand emblem decoration">
      <defs>
        <radialGradient id="markGlow" cx="0.55" cy="0.5" r="0.6">
          <stop offset="0" stop-color="#3a3637"/>
          <stop offset="1" stop-color="#231f20"/>
        </radialGradient>
      </defs>
      <rect width="380" height="412" fill="url(#markGlow)"/>
    </svg>
  </section>

</body>
</html>
```